ONE PAGE WEB DESIGN NEEDED for Finance Company

We need a web design (ONE PAGE DESIGN ONLY) for a new finance website called Brightwell Lending. Brightwell Lending helps customers get the right loan, whether its a home loan, investment loan, business loan etc.

You are required to come up with just the homepage design. Professionalism and quality is the key factors in the successful design.

Here are a few design questions to help you out:

-
What information should be used on the page?
Ive provided a document which outlines all the information needed to put on homepage (attached to the brief - called brightwell_page_info). Also see the Must Have section below on this brief.

-
What links should appear in the navigation/footer?:
The navigation should provide links to the following pages (NOTE: services link has subcategories):
1 Homepage
2 Services
- Home loans
- Investment loans
- Refinancing loans
- Business loans
3 About Us
4 FAQ
5 Contact Us

-
What colors should be used in the design?
Our company colors - Cyan: #2EADE3, Blue: #004B70, White. Feel free to submit designs with slight variations if you feel it improves the design.

-
What should the layout of the page be?
This is up to you to come up with - we are open to different layouts for the page design (as long as they capture the information effectively and making it easy to understand).

Target Market(s)

Potential Home owners, Families and Business Owners

Industry/Entity Type

Business

Requirements
Must have
• - Must contain our logo (attached as PNG and Illustrator file)
- Winning designer must supply a Photoshop file (PSD) that will allow us.
Nice to have
• - Should include photos/images of families, professional groups, tradespeople etc (you can use stock photos from PixQuarry and I will purchase them once you are selected as the winning design)
- Link to a loan calculator somewhere on front page with a button 'Find out how much you could borrow' (or maybe even try adding a loan calculator to the homepage if you think this would look good)
- Page should have a main headline "Finding the right loan for you" or "Brightwell Lending finds the right loan for our customers."
- Must include Accreditation logos somewhere on the homepage (will try and supply these soon)
Should not have
• - Poor quality designs will not be considered
- Do not use clipart

```html
<!DOCTYPE html>
<html lang="en">
<head>
<meta charset="utf-8">
<title>Brightwell Lending</title>
<link href="https://fonts.googleapis.com/css2?family=Ubuntu:wght@400;500;700&display=swap" rel="stylesheet">
<style>
:root{
  --cyan:#2eade3;
  --navy:#004b70;
  --sky:#7fbcd9;
  --icon:#74b4d4;
  --panel:#e3f2f9;
  --text:#444a4f;
  --muted:#a9b0b5;
  --white:#ffffff;
}
*{box-sizing:border-box;margin:0;padding:0}
html,body{width:1165px;height:1200px;overflow:hidden;background:var(--white);font-family:"Ubuntu",sans-serif;color:var(--text)}
.page{position:relative;width:1165px;height:1200px}

.site-header{position:absolute;left:0;top:0;width:1165px;height:120px;background:linear-gradient(#ffffff,#f1f2f3)}
.brand{position:absolute;left:35px;top:68px;display:flex;align-items:center;gap:10px;font-size:22px;font-weight:500;color:var(--navy)}
.brand-dot{width:16px;height:16px;border-radius:50%;background:var(--cyan)}
.header-phone{position:absolute;right:34px;top:40px;display:flex;align-items:center;gap:8px;font-size:20px;font-weight:500;color:var(--sky)}
.main-nav{position:absolute;right:34px;top:80px;display:flex;gap:33px;font-size:16px}
.main-nav a{color:var(--muted);text-decoration:none}
.main-nav a.is-active{color:var(--cyan)}

.stripe{position:absolute;left:0;width:1165px;height:9px;background:repeating-linear-gradient(90deg,var(--cyan) 0 63px,var(--navy) 63px 126px)}
.stripe-top{top:120px}
.stripe-bottom{top:566px}

.hero{position:absolute;left:0;top:129px;width:1165px;height:437px;background:linear-gradient(90deg,#e4edf0 0%,#f3f7f8 40%,#eef3f5 100%)}
.hero-photo{position:absolute;right:0;top:0;width:630px;height:437px;background:radial-gradient(ellipse at 55% 60%,#e8c9b4 0%,#d9b8a4 25%,#cfe0e8 60%,#eaf1f4 100%)}
.hero-title{position:absolute;left:32px;top:230px;font-size:54px;font-weight:500;color:var(--cyan);letter-spacing:.3px}
.hero-tagline{position:absolute;left:38px;top:302px;font-size:20px;font-weight:500;color:var(--navy)}

.intro{position:absolute;left:33px;top:614px;width:820px}
.intro h2{font-size:42px;font-weight:400;color:var(--sky);margin-bottom:18px}
.intro p{font-size:15.5px;line-height:21px;margin-bottom:21px;width:815px}

.side-box{position:absolute;left:883px;top:622px;width:248px;height:190px;border-radius:5px;overflow:hidden;background:var(--cyan);color:var(--white);text-align:center}
.side-box .calc{height:62px;background:var(--navy);border-bottom:4px solid #0a6691;font-size:20px;font-weight:700;line-height:62px;letter-spacing:.3px}
.side-box .contact-title{margin-top:17px;font-size:20px;font-weight:500}
.side-box .contact-phone{margin-top:14px;display:flex;justify-content:center;align-items:center;gap:8px;font-size:20px;font-weight:700}
.side-box .contact-note{margin-top:2px;font-size:12.5px;font-weight:700;letter-spacing:.8px}

.services{position:absolute;left:35px;top:849px;width:1096px;height:238px;background:var(--panel);border-radius:4px;box-shadow:0 3px 8px rgba(0,0,0,.08);display:flex}
.service{flex:1;position:relative;padding-top:22px}
.service + .service::before{content:"";position:absolute;left:0;top:40px;height:155px;width:1px;background:#cfe3ed}
.service svg{display:block;margin:0 auto;height:46px}
.service h3{text-align:center;font-size:19px;font-weight:500;color:var(--icon);margin-top:6px;letter-spacing:.3px}
.service ul{list-style:none;margin:14px 0 0 26px}
.service li{position:relative;padding-left:18px;font-size:15.5px;line-height:28px}
.service li::before{content:"";position:absolute;left:0;top:12px;width:6px;height:6px;border-radius:50%;background:var(--icon)}

.site-footer{position:absolute;left:35px;top:1134px;width:1096px;border-top:1px solid #e3e6e8}
.footer-nav{position:absolute;left:0;top:16px;display:flex;gap:12px;font-size:13px;letter-spacing:.6px}
.footer-nav a{color:var(--muted);text-decoration:none}
.copyright{position:absolute;right:0;top:16px;font-size:13px;letter-spacing:.6px;color:var(--muted)}
</style>
</head>
<body>
<div class="page">
  <header class="site-header">
    <div class="brand"><span class="brand-dot"></span>brightwell lending</div>
    <div class="header-phone">
      <svg width="18" height="18" viewBox="0 0 24 24"><path fill="#7fbcd9" d="M6.6 10.8a15 15 0 0 0 6.6 6.6l2.2-2.2c.3-.3.7-.4 1-.2 1.1.4 2.3.6 3.6.6.6 0 1 .4 1 1V20c0 .6-.4 1-1 1A17 17 0 0 1 3 4c0-.6.4-1 1-1h3.5c.6 0 1 .4 1 1 0 1.3.2 2.5.6 3.6.1.3 0 .7-.2 1z"/></svg>
      1800 555 246
    </div>
    <nav class="main-nav">
      <a href="#">Home</a><a href="#" class="is-active">Services</a><a href="#">About Us</a><a href="#">FAQ</a><a href="#">Contact Us</a>
    </nav>
  </header>
  <div class="stripe stripe-top"></div>

  <section class="hero">
    <div class="hero-photo" role="img" aria-label="Photo of a smiling family of four lying together on the floor"></div>
    <h1 class="hero-title">Brightwell Lending</h1>
    <p class="hero-tagline">Finds the right loan for our customers!</p>
  </section>
  <div class="stripe stripe-bottom"></div>

  <section class="intro">
    <h2>Why Choose Brightwell Lending?</h2>
    <p>At Brightwell Lending we work hard to find the right loan for our customers. We do that because we are backed by sound industry knowledge, professional experience and a great customer service approach. Brightwell Lending guarantees that we will always tailor the best solution for your individual lending needs.</p>
    <p>We can do that because we have access to a wide variety of lending options from major banks to non-bank lenders and we are committed to finding the right lending product for you.</p>
  </section>

  <aside class="side-box">
    <div class="calc">LOAN CALCULATOR</div>
    <div class="contact-title">CONTACT US</div>
    <div class="contact-phone">
      <svg width="18" height="18" viewBox="0 0 24 24"><path fill="#ffffff" d="M6.6 10.8a15 15 0 0 0 6.6 6.6l2.2-2.2c.3-.3.7-.4 1-.2 1.1.4 2.3.6 3.6.6.6 0 1 .4 1 1V20c0 .6-.4 1-1 1A17 17 0 0 1 3 4c0-.6.4-1 1-1h3.5c.6 0 1 .4 1 1 0 1.3.2 2.5.6 3.6.1.3 0 .7-.2 1z"/></svg>
      1800 555 246
    </div>
    <div class="contact-note">TO FIND OUT MORE</div>
  </aside>

  <section class="services">
    <div class="service">
      <svg viewBox="0 0 52 46" width="52"><path fill="#74b4d4" d="M26 2 2 24h7v20h13V31h8v13h13V24h7L38 13V5h-6v3z"/></svg>
      <h3>HOME LOAN</h3>
      <ul><li>Home buyers</li><li>First home buyers</li><li>Over 20 lenders</li></ul>
    </div>
    <div class="service">
      <svg viewBox="0 0 46 46" width="46"><circle cx="23" cy="23" r="22" fill="#74b4d4"/><text x="23" y="33" text-anchor="middle" font-family="Ubuntu,sans-serif" font-size="30" font-weight="700" fill="#e3f2f9">$</text></svg>
      <h3>INVESTMENT LOAN</h3>
      <ul><li>Property investment loans</li><li>Interest only loans</li></ul>
    </div>
    <div class="service">
      <svg viewBox="0 0 68 46" width="68"><circle cx="36" cy="11" r="10" fill="#74b4d4"/><text x="36" y="16" text-anchor="middle" font-family="Ubuntu,sans-serif" font-size="14" font-weight="700" fill="#e3f2f9">$</text><path fill="#74b4d4" d="M2 36c8-6 16-9 24-7l14 2c3 1 3 5 0 5H28l13 1 20-9c4-1 6 2 3 4L42 44c-6 2-20 1-28-1l-12 1z"/></svg>
      <h3>REFINANCING</h3>
      <ul><li>Refinancing for the best rate</li><li>Upsizing or downsizing</li><li>Change from a variable to a fixed rate</li></ul>
    </div>
    <div class="service">
      <svg viewBox="0 0 46 46" width="46"><path fill="#74b4d4" d="M23 2 44 44H2z"/><path stroke="#e3f2f9" stroke-width="2" d="M10 28h26M6 36h34M23 8 16 44M23 8l7 36"/></svg>
      <h3>BUSINESS LOAN</h3>
      <ul><li>Long term</li><li>Short term</li><li>Equipment and Leasing</li></ul>
    </div>
  </section>

  <footer class="site-footer">
    <nav class="footer-nav"><a href="#">Home</a><a href="#">Services</a><a href="#">About Us</a><a href="#">FAQ</a><a href="#">Contact Us</a></nav>
    <div class="copyright">Copyrights Brightwell Lending</div>
  </footer>
</div>
</body>
</html>
```